PDBA website design

We need a page template website design for a cms website. Please see the brief attached for the details.
The client is the Pacific Downhorn Breeders Association which is an organisation promoting the White Suffolk Sheep Breed within Australia.

Reason: So that my top few designs can make changes and re-submit.

Target Market(s)

See attached brief

```html
<!DOCTYPE html>
<html lang="en">
<head>
<meta charset="utf-8">
<title>Pacific Downhorn Breeders Association</title>
<link rel="stylesheet" href="https://fonts.googleapis.com/css2?family=Open+Sans:wght@400;600;700&display=swap">
<style>
:root{
  --green:#0fa14a;
  --green-dark:#0a7a3a;
  --green-text:#1a8c3c;
  --nav-active:#2b2b2b;
  --text:#6b6b6b;
  --text-dark:#2c2c2c;
  --muted:#9a9a9a;
  --rule:#dcdcdc;
  --tile-top:#a3a3a3;
  --tile-bottom:#8a8a8a;
  --band:#f1f1f1;
  --footer:#2a2a2a;
  --white:#ffffff;
}
*{box-sizing:border-box;margin:0;padding:0}
html,body{width:1013px;height:1200px;overflow:hidden}
body{font-family:"Open Sans",Arial,sans-serif;background:var(--white);color:var(--text);position:relative}
.wrap{position:absolute;left:85px;width:845px}

.site-header{position:absolute;top:0;left:0;width:1013px;height:122px}
.brand{position:absolute;left:88px;top:26px;display:flex;align-items:center;gap:10px}
.brand-mark{width:46px;height:46px;border-radius:50%;background:var(--green)}
.brand-name{font-size:24px;font-weight:700;color:var(--green-dark);line-height:1.05}
.brand-name small{display:block;font-size:12px;font-weight:400;color:var(--green-dark)}
.contact-top{position:absolute;right:83px;top:26px;text-align:right}
.contact-top .addr{font-size:11px;color:var(--text);padding-right:28px}
.contact-top .call{font-size:16px;font-weight:600;color:var(--green-text);padding-right:28px}
.contact-top .mail-icon{position:absolute;right:0;top:4px;width:20px;height:24px;background:#b5b5b5;border-radius:2px}
.org-title{position:absolute;right:83px;top:64px;font-size:31px;font-weight:400;color:#cfcfcf;letter-spacing:.2px}

.main-nav{position:absolute;top:122px;left:0;width:1013px;height:37px;background:var(--green)}
.main-nav ul{list-style:none;display:flex;position:absolute;left:85px;height:37px;border-left:1px solid var(--green-dark)}
.main-nav li{height:37px;line-height:37px;padding:0 18px;font-size:12.5px;color:var(--white);border-right:1px solid var(--green-dark);text-transform:uppercase}
.main-nav li.active{background:var(--nav-active)}
.dropdown{position:absolute;left:161px;top:159px;width:117px;background:var(--nav-active);padding:3px 0 4px;z-index:2}
.dropdown a{display:block;font-size:10.5px;color:var(--white);padding:2px 12px;text-decoration:none}

.hero{position:absolute;top:159px;left:0;width:1013px;height:371px;background:linear-gradient(180deg,#b9cfe0 0%,#8fa86a 32%,#4d6b34 55%,#6fae3c 72%,#5fbb2d 100%)}
.hero-caption{position:absolute;left:309px;top:167px;background:rgba(30,30,30,.55);color:var(--white);font-size:22px;padding:2px 11px}
.hero-arrow{position:absolute;top:171px;width:26px;height:26px;border-radius:50%;background:var(--white)}
.hero-arrow.prev{left:85px}.hero-arrow.next{right:85px}
.hero-arrow svg{width:26px;height:26px}

.intro{position:absolute;left:85px;top:557px;width:610px}
.intro h1{font-size:22px;font-weight:400;color:var(--green-dark);margin-bottom:5px}
.intro p{font-size:12.5px;line-height:19.5px;margin-bottom:16px}
.intro h2{font-size:13.5px;font-weight:600;color:var(--text-dark);margin-bottom:8px}
.aims{list-style:none}
.aims li{position:relative;font-size:11.5px;line-height:16px;padding-left:18px;margin-bottom:7px}
.aims li::before{content:"›";position:absolute;left:2px;top:-2px;font-size:15px;color:#888}

.quick-links{position:absolute;left:724px;top:556px;width:205px}
.tile{display:flex;align-items:center;background:linear-gradient(180deg,var(--tile-top),var(--tile-bottom));color:var(--white);margin-bottom:4px;padding-left:12px}
.tile.tall{height:68px}.tile.short{height:50px}
.tile svg{width:28px;height:28px;flex:none;margin-right:12px}
.tile span{font-size:21px;line-height:24px}

.divider{position:absolute;left:85px;top:907px;width:845px;height:1px;background:var(--rule)}
.sponsors{position:absolute;left:85px;top:932px;width:845px;text-align:center}
.sponsors h3{font-size:12px;font-weight:400;color:var(--text);margin-bottom:20px}
.sponsor-row{display:flex;justify-content:center;gap:32px;align-items:center}
.sponsor{display:flex;align-items:center;gap:6px;font-size:18px;font-weight:600;color:#a8a8a8}
.sponsor i{width:18px;height:18px;border-radius:50%;background:#b0b0b0;display:block}

.contact-band{position:absolute;top:1033px;left:0;width:1013px;height:81px;background:var(--band)}
.contact-item{position:absolute;top:24px;display:flex;gap:12px;font-size:11.5px;line-height:19px;color:var(--text)}
.contact-item svg{width:22px;height:22px;flex:none;margin-top:-1px}

.site-footer{position:absolute;top:1114px;left:0;width:1013px;height:86px;background:var(--footer)}
.footer-nav{position:absolute;left:85px;top:19px;font-size:11px;color:#cfcfcf}
.footer-nav span{margin:0 6px;color:#888}
.copyright{position:absolute;left:85px;top:50px;font-size:11px;color:#cfcfcf}
.follow{position:absolute;right:84px;top:27px;width:104px;height:32px;background:#e8ecf3;border:1px solid #9aa;display:flex;align-items:center;gap:6px;padding-left:6px;font-size:11px;font-weight:600;color:#3a5a96}
.follow i{width:16px;height:16px;background:#3a5a96;display:block}
</style>
</head>
<body>

<header class="site-header">
  <div class="brand">
    <div class="brand-mark"></div>
    <div class="brand-name">Pacific Downhorn<small>Breeders Association</small></div>
  </div>
  <div class="contact-top">
    <div class="addr">PO Box 427, Marlow Vale, SA 5190</div>
    <div class="call">Call : 08 7300 4418</div>
    <div class="mail-icon"></div>
  </div>
  <div class="org-title">Pacific Downhorn Breeders Association</div>
</header>

<nav class="main-nav">
  <ul>
    <li>Home</li><li class="active">About</li><li>Search</li><li>Member Services</li><li>Stud Pages</li><li>News</li><li>Sales</li><li>Links</li><li>Contact</li>
  </ul>
</nav>

<section class="hero" role="img" aria-label="Flock of white sheep grazing on green pasture with forested hills behind">
  <div class="hero-arrow prev"><svg viewBox="0 0 26 26"><path d="M15 8l-5 5 5 5" fill="none" stroke="#888" stroke-width="1.5"/></svg></div>
  <div class="hero-caption">Donec a ipsum ac nisl faucibus ornare</div>
  <div class="hero-arrow next"><svg viewBox="0 0 26 26"><path d="M11 8l5 5-5 5" fill="none" stroke="#888" stroke-width="1.5"/></svg></div>
</section>

<div class="dropdown"><a>» Breed</a><a>» Genetic Testing</a></div>

<main class="intro">
  <h1>Welcome to Pacific Downhorn Breeders Association</h1>
  <p>The White Suffolk is an Australian breed developed for Australian conditions. The White Suffolk is proving to be the ideal prime lamb terminal sire in wide-ranging areas and environments of Australia. It is giving outstanding results in the dry, arid, pastoral zones; all types of agricultural, mixed farming areas; and also in higher rainfall districts.</p>
  <h2>The PACIFIC DOWNHORN BREEDERS ASSOCIATION aims to:</h2>
  <ul class="aims">
    <li>Be at the forefront of marketing and promotion of the White Suffolk breed</li>
    <li>Better educate our members and commerical breeders on providing superior genetics to the Australian lamb industry</li>
    <li>Continue to develop the White Suffolk breed to the advantage of all involved in the Australian lamb industry</li>
    <li>Encourage extensive use of genetic evaluation and continue to benchmark the White Suffolk breed to become the leading performance breed</li>
    <li>Remain at the forefront of recent technological advances within the livestock industry</li>
    <li>Promote the White Suffolk as an alternative maternal sire</li>
  </ul>
</main>

<aside class="quick-links">
  <div class="tile tall"><svg viewBox="0 0 28 28"><circle cx="14" cy="14" r="12" fill="none" stroke="#fff" stroke-width="3"/><circle cx="14" cy="14" r="5" fill="none" stroke="#fff" stroke-width="3"/><path d="M6 6l5 5M22 6l-5 5M6 22l5-5M22 22l-5-5" stroke="#fff" stroke-width="3"/></svg><span>Prime Lamb<br>Helpline</span></div>
  <div class="tile short"><svg viewBox="0 0 28 28"><rect x="2" y="5" width="24" height="20" fill="none" stroke="#fff" stroke-width="2"/><rect x="2" y="5" width="24" height="5" fill="#fff"/><path d="M6 14h3M12 14h3M18 14h3M6 19h3M12 19h3M18 19h3" stroke="#fff" stroke-width="3"/></svg><span>Events</span></div>
  <div class="tile tall"><svg viewBox="0 0 28 28"><circle cx="10" cy="10" r="4" fill="#fff"/><circle cx="19" cy="9" r="3.5" fill="#fff"/><path d="M2 24c0-6 4-9 8-9s8 3 8 9zM17 14c4 0 9 2 9 8h-7" fill="#fff"/></svg><span>Members<br>Resources</span></div>
  <div class="tile tall"><svg viewBox="0 0 28 28"><circle cx="14" cy="8" r="6" fill="#fff"/><rect x="12.5" y="12" width="3" height="14" fill="#fff"/><rect x="15" y="19" width="4" height="2.5" fill="#fff"/></svg><span>WebManager<br>Login</span></div>
  <div class="tile short"><svg viewBox="0 0 28 28"><rect x="2" y="4" width="24" height="20" fill="none" stroke="#fff" stroke-width="2"/><rect x="6" y="9" width="7" height="7" fill="#fff"/><path d="M15 10h7M15 14h7M6 19h16" stroke="#fff" stroke-width="2"/></svg><span>Latest News</span></div>
</aside>

<div class="divider"></div>

<section class="sponsors">
  <h3>SPONSORS</h3>
  <div class="sponsor-row">
    <div class="sponsor"><i></i>Tallyrow</div>
    <div class="sponsor">Penwick</div>
    <div class="sponsor">Fieldgate</div>
    <div class="sponsor">Brindlewood</div>
    <div class="sponsor"><i></i>Orrin</div>
    <div class="sponsor">Northmead</div>
  </div>
</section>

<section class="contact-band">
  <div class="contact-item" style="left:94px"><svg viewBox="0 0 22 22"><rect x="3" y="2" width="16" height="19" fill="none" stroke="#999" stroke-width="2"/><path d="M9 2v9l2-2 2 2V2" fill="#999"/></svg><div>PO Box 427, Marlow Vale,<br>SA 5190</div></div>
  <div class="contact-item" style="left:313px"><svg viewBox="0 0 22 22"><path d="M4 3c-2 2 0 8 5 13s11 7 13 5l-4-5-3 2c-2-1-5-4-6-6l2-3z" fill="#999"/></svg><div>Phone: (08) 7300 4418</div></div>
  <div class="contact-item" style="left:526px"><svg viewBox="0 0 22 22"><rect x="2" y="8" width="18" height="13" fill="none" stroke="#999" stroke-width="2"/><rect x="7" y="2" width="10" height="8" fill="#999"/><path d="M9 13h2M13 13h2M9 17h2M13 17h2" stroke="#999" stroke-width="2"/></svg><div>Fax : (08) 7300 4419</div></div>
  <div class="contact-item" style="left:709px"><svg viewBox="0 0 22 22"><rect x="1" y="5" width="20" height="13" fill="#999"/><path d="M1 5l10 7 10-7" fill="none" stroke="#f1f1f1" stroke-width="1.5"/></svg><div>E-mail : office@pacificdownhorn.org</div></div>
</section>

<footer class="site-footer">
  <div class="footer-nav">Home<span>|</span>About<span>|</span>Search<span>|</span>Member Services<span>|</span>Stud Pages<span>|</span>News<span>|</span>Sales<span>|</span>Links<span>|</span>Contact</div>
  <div class="copyright">Copyright &copy; 2014 &nbsp;pacific downhorn. &nbsp;All rights reserved.</div>
  <div class="follow"><i></i>Follow us online</div>
</footer>

</body>
</html>
```